依頼詳細
今回は、トップページデザインの募集になります。
レスポンシブデザインのサイトで、bootstrap4を利用しコーディングする予定になります。
デザイン幅は2000px、コンテンツの幅はbootstrap4デフォルトの1110pxを基準としてください。ただし最近のデザインの流行を取りいれて、フルワイドや、1200~15000px程度の幅のコンテンツをバランスよくレイアウトしてください。
コンテンツ配置は基本12分割になります。がデザインによっては、多少逸脱してもかまいません。
念のため、サンプルのPSDデータを添付しますので、参照ください。

本文のフォントはゴシック系は游ゴシック、メイリオ、明朝系は遊明朝でお願いします。
飾り文字はフリーフォントか、googleフォントを利用してください。

メイン画像部分・グローバルメニューは、ワイド適用でお願いします。

資料上はサイト名(社名)や住所などは伏字にしております。ご提案時点ではそのまま作成をお願いします。当選確定後、本内容に修正をお願いいたします。

当選の方は、希望があれば引き続き下層ページの作成及びコーディング作業を依頼可能です。
不明点、質問などありましたらメッセージ等でご連絡ください。

・カラー
青系(爽やかなイメージ)

・掲載画像
必ず添付ファイルを使用してください。
また、雰囲気が合っていれば、指定外の画像を背景などに使用いただいてもOKです。

・その他
内容詳細に関しては、別添のExcel資料を参照してください。
ページ数
1ページ
希望イメージ
シンプル 複雑
単色 カラフル
暗い 明るい
日常 高級
遊び心 厳粛
未来的 伝統的
女性的 男性的
希望する色
青系、水色系
納品ファイル
• 高解像度JPG (.jpg)
• フォトショップ形式 (.psd)
補足説明
納品ファイルは、PDF及びクライアント表示確認用のJPGを準備お願いします。
■ 選んだ理由

今回は、贅沢さや豪華さをイメージさせる洗練された先進的なデザインを希望しており、見た目が大事な案件でした。
業界的に国内外問わず「サイトの見た目」をかなり重要視しているため、"見栄えのするデザイン"というところに重きを置いてクライアントとの折衝の結果、skytrailふじさわ様を選定させていただきました。

■ 提案者全員のお礼・コメント

どの案も制作意図を組んでいただきとてもよかったのですが、今回はskytrailふじさわ様を当選とさせていただきました。
皆様ご提案ありがとうございました。
今後ともご提案宜しくお願いいたします。

```html
<!DOCTYPE html>
<html lang="ja">
<head>
<meta charset="utf-8">
<title>Safety High Quality</title>
<link href="https://fonts.googleapis.com/css2?family=Josefin+Sans:wght@300;400;600&family=Noto+Sans+JP:wght@400;500;700&family=Noto+Serif+JP:wght@500&display=swap" rel="stylesheet">
<style>
:root{
  --blue:#4ec2ea;
  --blue-deep:#1f7fc4;
  --navy:#1d3a5a;
  --red:#e2263d;
  --teal:#1e8f8a;
  --ink:#333;
  --grey:#888;
  --white:#fff;
  --line:#d8d8d8;
}
*{margin:0;padding:0;box-sizing:border-box}
html,body{width:1200px;height:4108px;overflow:hidden}
body{position:relative;background:var(--white);font-family:"Noto Sans JP",sans-serif;color:var(--ink)}
.abs{position:absolute}
.en{font-family:"Josefin Sans",sans-serif}

/* header */
.site-header{left:0;top:0;width:1200px;height:80px;background:var(--white);z-index:5}
.logo{left:28px;top:24px;font-family:"Josefin Sans",sans-serif;font-weight:600;font-size:26px;color:var(--navy)}
.gnav{right:20px;top:8px;display:flex}
.gnav li{list-style:none;width:96px;text-align:center;position:relative;padding-top:16px}
.gnav .tab{position:absolute;top:0;left:20px;width:56px;height:12px;font-size:8px;color:#fff;line-height:12px}
.gnav .en-label{font-family:"Josefin Sans",sans-serif;font-size:14px;color:var(--navy);letter-spacing:1px;display:block}
.gnav .jp-label{font-size:9px;color:var(--grey)}
.gnav li.current{border-bottom:2px solid var(--navy)}

/* hero */
.hero{left:0;top:80px;width:1200px;height:800px;overflow:hidden}
.hero-photo{width:100%;height:100%;background:linear-gradient(180deg,#3a8ee0 0%,#7cc3f2 25%,#d9eef8 38%,#9fb9a0 48%,#3a7fb4 62%,#1f6aa6 80%,#2a7fb8 100%)}
.hero-veil{left:0;top:0;width:1200px;height:800px}
.hero-title{right:80px;top:100px;font-family:"Josefin Sans",sans-serif;font-weight:400;font-size:74px;color:#fff;letter-spacing:1px}
.hero-sub{right:80px;top:240px;font-size:24px;color:#fff;letter-spacing:2px}
.hero-ghost{left:20px;top:210px;font-family:"Josefin Sans",sans-serif;font-weight:300;font-size:150px;line-height:120px;color:transparent;-webkit-text-stroke:1.5px rgba(255,255,255,.75)}

/* intro */
.intro-lead{left:0;top:905px;width:1200px;text-align:center;font-family:"Noto Serif JP",serif;font-size:26px;color:var(--red);letter-spacing:2px}
.intro-text{left:0;top:965px;width:1200px;text-align:center;font-size:14px;line-height:26px;color:var(--ink)}

/* cards */
.card{top:1160px;width:592px;height:420px;overflow:hidden}
.card-photo{width:100%;height:100%}
.card-title{left:0;top:90px;width:100%;text-align:center;font-family:"Josefin Sans",sans-serif;font-size:50px;color:var(--navy);letter-spacing:2px}
.card-band{left:40px;top:150px;width:512px;height:70px;background:rgba(255,255,255,.6);font-size:13px;text-align:center;line-height:20px;padding-top:16px;color:var(--navy)}
.card-band small{display:block;font-size:12px}
.more{width:150px;height:48px;background:var(--red);color:#fff;font-family:"Josefin Sans",sans-serif;font-size:16px;display:flex;align-items:center;justify-content:center;gap:16px;letter-spacing:1px}
.card .more{right:0;bottom:0}

/* bus */
.bus-band{left:0;top:1620px;width:1200px;height:800px;background:var(--blue);clip-path:polygon(0 0,100% 60px,100% 100%,0 88%)}
.photo-frame{background:#fff;padding:14px;box-shadow:0 6px 16px rgba(0,0,0,.25)}
.photo-frame div{width:100%;height:100%}
.bus-main{left:40px;top:1792px;width:790px;height:510px;transform:rotate(-1.5deg)}
.bus-sub{left:780px;top:2120px;width:390px;height:220px;transform:rotate(2deg)}
.bus-label{left:960px;top:1850px;text-align:center;color:#fff}
.bus-label .en{font-size:44px;font-weight:300;letter-spacing:2px}
.bus-label .jp{font-size:11px;border-top:1px solid #fff;padding-top:4px;margin-top:2px}
.bus-more{left:525px;top:2344px}

/* information */
.info-title{left:90px;top:2560px;color:var(--navy)}
.info-title .en{font-size:40px;font-weight:400;letter-spacing:1px}
.info-title .jp{font-size:11px;color:var(--grey);margin-top:2px}
.info-list{left:540px;top:2600px;width:560px;list-style:none}
.info-list li{display:flex;align-items:center;height:60px;border-bottom:1px solid var(--line);font-size:13px}
.info-list .date{width:110px;color:var(--navy);font-family:"Josefin Sans",sans-serif;font-size:15px}
.info-list .tag{width:42px;height:16px;margin-right:18px;font-size:9px;text-align:center;line-height:16px;color:#fff}
.tag-new{background:var(--red)}
.tag-none{visibility:hidden}

/* contact */
.contact-photo{left:160px;top:2860px;width:880px;height:660px;background:linear-gradient(180deg,#eef3f6 0%,#c9d7e2 35%,#b9a88f 60%,#8d8f92 80%,#6a6f74 100%)}
.contact-title{left:470px;top:2935px;color:var(--navy);text-align:center}
.contact-title .en{font-size:52px;letter-spacing:2px}
.contact-title .jp{font-size:11px;color:var(--grey)}
.contact-row{left:392px;width:410px;height:90px;background:rgba(255,255,255,.78);display:flex;align-items:center;gap:24px;padding-left:28px;color:var(--navy)}
.contact-row .num{font-family:"Josefin Sans",sans-serif;font-size:34px;letter-spacing:2px}
.contact-mail{height:120px}
.contact-mail .num{font-size:32px}
.contact-mail small{display:block;font-family:"Noto Sans JP",sans-serif;font-size:11px;letter-spacing:0}
.bubble{left:1020px;top:2870px;width:150px;height:110px;background:#fff;border:2px solid var(--blue);border-radius:50%;display:flex;align-items:center;justify-content:center;text-align:center;font-size:11px;line-height:16px;color:var(--blue-deep)}
.contact-arrow{left:800px;top:3310px;width:0;height:0;border-left:48px solid transparent;border-bottom:48px solid var(--red)}

/* footer */
.site-footer{left:0;top:3580px;width:1200px;height:480px;overflow:hidden}
.footer-photo{width:100%;height:100%;background:linear-gradient(180deg,#4a8fc7 0%,#2c5d8f 45%,#1d3958 75%,#172b45 100%);clip-path:polygon(0 8%,100% 0,100% 100%,0 100%)}
.footer-info{left:70px;top:210px;color:#fff;font-size:17px;line-height:26px}
.footer-info .name{font-size:19px;font-weight:700;margin-bottom:4px}
.footer-nav{left:1000px;top:240px;list-style:none;color:#fff;font-size:15px;line-height:30px}
.footer-nav li::before{content:"";display:inline-block;width:7px;height:7px;background:var(--red);margin-right:10px;vertical-align:middle}
.copyright{left:0;top:4060px;width:1200px;height:48px;background:var(--navy);color:#fff;font-size:11px;text-align:center;line-height:48px}
</style>
</head>
<body>

<header class="abs site-header">
  <div class="abs logo">LOGO</div>
  <ul class="abs gnav">
    <li class="current"><span class="en-label">HOME</span><span class="jp-label">ホーム</span></li>
    <li><span class="en-label">COMPANY</span><span class="jp-label">会社概要</span></li>
    <li><span class="tab" style="background:var(--red)">採用</span><span class="en-label">BUS</span><span class="jp-label">バスのご紹介</span></li>
    <li><span class="tab" style="background:var(--teal)">お知らせ</span><span class="en-label">SAFETY</span><span class="jp-label">安全への取組</span></li>
    <li><span class="tab" style="background:var(--navy)">アクセス</span><span class="en-label">CONTACT</span><span class="jp-label">お問合わせ</span></li>
  </ul>
</header>

<section class="abs hero">
  <div class="hero-photo" role="img" aria-label="Aerial view of a waterfront city with high-rise buildings, canals and blue sky"></div>
  <svg class="abs hero-veil" viewBox="0 0 1200 800" width="1200" height="800">
    <polygon points="560,0 1200,0 1200,400 760,400" fill="#5aa7e6" opacity=".35"/>
    <path d="M0 640 Q600 860 1200 600 L1200 800 L0 800 Z" fill="#fff"/>
  </svg>
  <div class="abs hero-ghost">Safety<br>High<br>Quality</div>
  <h1 class="abs hero-title">Safety High Quality</h1>
  <p class="abs hero-sub">○○○○○○○○○○ Company Limited</p>
</section>

<section>
  <h2 class="abs intro-lead">より一層安全・安心なお客様サービスの実現へ</h2>
  <p class="abs intro-text">○○○○○は、"Safety"と"High Quality"をモットーとし、<br>これからも「確かな安全・安心」と「最高水準のサービス」で快適な旅をお手伝いします。</p>
</section>

<section class="abs card" style="left:0">
  <div class="card-photo" role="img" aria-label="City skyline by the sea under a blue sky" style="background:linear-gradient(180deg,#8fc6ee 0%,#cfe6f5 40%,#8aa2b4 62%,#3b86b8 80%,#2b6f98 100%)"></div>
  <div class="abs card-title">COMPANY</div>
  <div class="abs card-band">会社概要<small>私たちの理念と会社の歩みをご紹介します。</small></div>
  <div class="abs more">MORE <span>»</span></div>
</section>

<section class="abs card" style="left:608px">
  <div class="card-photo" role="img" aria-label="Harbour with moored yachts in front of a city skyline" style="background:linear-gradient(180deg,#5aa3e0 0%,#bfe0f6 40%,#9ab0c0 60%,#e9eef2 75%,#6a95b6 100%)"></div>
  <div class="abs card-title">SAFETY</div>
  <div class="abs card-band">安全への取組<small>安全・安心のために取り組む活動をご紹介しています。</small></div>
  <div class="abs more">MORE <span>»</span></div>
</section>

<div class="abs bus-band"></div>
<div class="abs photo-frame bus-main"><div role="img" aria-label="White coach bus parked on a palm-lined street in front of a building" style="background:linear-gradient(180deg,#7fbbe8 0%,#d6e9f5 35%,#c8b89a 55%,#8c8f93 78%,#5f6469 100%)"></div></div>
<div class="abs photo-frame bus-sub"><div role="img" aria-label="Several coach buses lined up in a parking lot" style="background:linear-gradient(180deg,#6eb3e6 0%,#c6e2f4 45%,#b5bcc2 65%,#7d8388 100%)"></div></div>
<div class="abs bus-label"><div class="en">BUS</div><div class="jp">バスのご紹介</div></div>
<div class="abs more bus-more">MORE <span>»</span></div>

<section>
  <div class="abs info-title"><div class="en">INFORMATION</div><div class="jp">○○○○○からのお知らせ</div></div>
  <ul class="abs info-list">
    <li><span class="date">2020/3/1</span><span class="tag tag-new">NEW</span>ホームページをリニューアルしました。</li>
    <li><span class="date">2020/3/1</span><span class="tag tag-none">NEW</span>ホームページをリニューアルしました。</li>
    <li><span class="date">2020/3/1</span><span class="tag tag-none">NEW</span>ホームページをリニューアルしました。</li>
  </ul>
</section>

<section>
  <div class="abs contact-photo" role="img" aria-label="Bus terminal with a coach in front of city buildings and flags"></div>
  <div class="abs contact-title"><div class="en">CONTACT</div><div class="jp">お問い合わせ</div></div>
  <div class="abs contact-row" style="top:3060px">
    <svg width="40" height="40" viewBox="0 0 24 24"><path fill="#1d3a5a" d="M6.6 10.8c1.4 2.8 3.8 5.1 6.6 6.6l2.2-2.2c.3-.3.7-.4 1-.2 1.1.4 2.3.6 3.6.6.6 0 1 .4 1 1V20c0 .6-.4 1-1 1C10.6 21 3 13.4 3 4c0-.6.4-1 1-1h3.5c.6 0 1 .4 1 1 0 1.2.2 2.4.6 3.6.1.3 0 .7-.2 1z"/></svg>
    <span class="num">012-345-6789</span>
  </div>
  <div class="abs contact-row" style="top:3180px">
    <svg width="40" height="40" viewBox="0 0 24 24"><path fill="#1d3a5a" d="M7 3h10v4H7zM4 8h16a2 2 0 0 1 2 2v6h-4v4H6v-4H2v-6a2 2 0 0 1 2-2zm4 7v3h8v-3z"/></svg>
    <span class="num">098-765-4321</span>
  </div>
  <div class="abs contact-row contact-mail" style="top:3310px">
    <svg width="44" height="36" viewBox="0 0 24 20"><rect x="1" y="2" width="22" height="16" fill="none" stroke="#1d3a5a" stroke-width="2"/><path d="M1 3l11 8 11-8" fill="none" stroke="#1d3a5a" stroke-width="2"/></svg>
    <span class="num">MAIL<small>お問い合わせフォームはこちら</small></span>
  </div>
  <div class="abs contact-arrow"></div>
  <div class="abs bubble">お気軽に<br>お問い合わせ<br>ください</div>
</section>

<footer class="abs site-footer">
  <div class="footer-photo" role="img" aria-label="City skyline at dusk"></div>
  <div class="abs footer-info">
    <div class="name">○○○○○○○○株式会社</div>
    〒123-4567 大阪府○○市○町<br>TEL 012-345-6789<br>FAX 098-765-4321
  </div>
  <ul class="abs footer-nav">
    <li>ホーム</li><li>会社概要</li><li>バスのご紹介</li><li>安全の取組み</li><li>お問い合わせ</li>
  </ul>
</footer>
<div class="abs copyright">©2020 ○○○○株式会社</div>

</body>
</html>
```